Website Design for a DJ Entertainment and Productions Comany

We are a full service DJ Entertainment and Productions company looking to have a strong presence in our local market and need a phenomenal website design to drive clients to the site but then also keep them there. We cater to all types of different events varying from weddings to proms to corporate events, birthdays, bar mitzvah's and so on and so on. We also do full lighting for any type of event and we also offer a photobooth service for various events. The best way to get an idea of the services that we offer is to visit http://www.velmorahaus.com/index.html This site is NOT our own but only linked as an example of what we do and will give you an overall overview of what we offer.
We are looking for pure creativity as there are multiple facets to our company and the services we offer. On the one hand we can provide a night club party atmosphere for Proms or dances but on the other hand we also provide professional full service emcee/DJ for weddings and formal events. The key for this site would be to have the pages for each category match the look and feel of the actual service provided, ie the Wedding page will look more refined and professional vs the Party DJ page. Each page needs to fit the overall feel of the Company and Logo though. Here is a list of pages that we would need to have on the final site.
HOME PAGE
PROFESSINAL DJS- This will have info. and pricing of our DJ services for everything but weddings. Should have pics and videos somewhere on this page.
WEDDINGS- All wedding package pricing and info. This page should look more elegant, formal and high class compared to the other pages.
PHOTOBOOTH-Page with info, pricing on photobooth see http://www.glintrivuphotobooth.com/
LIGHTING DESIGN-Info on our lighting services along with pricing
CORPORATE EVENTS-Info on services and pricing for corporate events. This page should seem more professional centered towards business clientele.
CLIENT LOGIN-Page for existing clients to logon to update info and fill out information.
CONNECT WITH US- Social Media links.
Our logo was submitted through Pixel Harbor but I am open to suggestions on revisions if you feel the need to change it. Color is also not set in stone.
I have increased my budget $200 more. Please submit your designs for review, deadline is approaching quickly. Also see brief for revisions.
Thank you.
Target Market(s)
Broad Range but usually Under 40
Industry/Entity Type
Night Club
Look and feel

```html
<!DOCTYPE html>
<html lang="en">
<head>
<meta charset="utf-8">
<title>Nocturne Entertainment &amp; Productions</title>
<link href="https://fonts.googleapis.com/css2?family=Signika:wght@400;600;700&family=Arimo:wght@400;700&display=swap" rel="stylesheet">
<style>
:root{
  --black:#050505;
  --panel:#1b1b1b;
  --rule:#262626;
  --red:#e8212a;
  --blue:#3cb6e8;
  --gold:#f6b23c;
  --text:#d6d6d6;
  --green:#1d7a5a;
  --footer:#d9d9d9;
}
*{box-sizing:border-box;margin:0;padding:0}
html,body{width:923px;height:1200px;overflow:hidden;background:#fff}
.stage{position:absolute;left:0;top:0;width:1000px;height:1300px;transform:scale(0.923);transform-origin:0 0;background:#fff;overflow:hidden}
.page{position:absolute;left:20px;top:0;width:960px;height:1288px;background:var(--black);font-family:"Arimo",Arial,sans-serif;color:var(--text);overflow:hidden}
.abs{position:absolute}
.header{left:0;top:0;width:960px;height:100px;background:linear-gradient(#1a1a1a,#0a0a0a)}
.brand{left:34px;top:14px;display:flex;align-items:center;gap:14px}
.brand-mark{width:60px;height:60px;border-radius:50%;background:var(--red)}
.brand-name{font-family:"Signika",sans-serif;font-weight:700;font-size:34px;color:var(--red);line-height:1}
.brand-sub{font-family:"Signika",sans-serif;font-weight:700;font-size:11px;color:var(--red);letter-spacing:.3px}
.search{left:650px;top:33px;width:260px;height:34px;border:2px solid #555;border-radius:3px;background:linear-gradient(#3a3a3a,#222);display:flex;align-items:center;gap:12px;padding-left:8px;font-size:14px;color:#bbb}
.nav{left:0;top:100px;width:960px;height:57px;background:#000;display:flex;align-items:center;font-family:"Signika",sans-serif;font-weight:700;font-size:15px;color:#fff}
.nav a{color:#fff;text-decoration:none;margin-right:27px}
.nav .active{background:linear-gradient(#0e3a2c,var(--green));height:57px;line-height:57px;padding:0 12px;margin-left:24px;margin-right:15px}
.band{left:0;width:960px;height:8px;background:linear-gradient(#8a9096,#4a5056)}
.hero{left:0;top:165px;width:960px;height:300px;background:linear-gradient(100deg,#121212 0%,#3a3a3a 55%,#5a5a5a 100%);overflow:hidden}
.hero-photo{left:640px;top:0;width:320px;height:300px;background:radial-gradient(circle at 60% 40%,#b89a88,#6d625c 55%,#3d3d3d)}
.hero-title-bar{left:84px;top:56px;width:466px;height:58px;background:#0b0b0b}
.hero-title{left:84px;top:56px;font-family:"Signika",sans-serif;font-weight:700;font-size:50px;line-height:58px;color:#e0e0e0}
.hero-lead{left:86px;top:126px;font-size:16px;color:var(--gold)}
.hero-body{left:102px;top:166px;width:440px;font-size:12px;line-height:18.5px;color:#aaa}
.chev{left:14px;top:270px}
.content{left:0;top:472px;width:960px;height:700px;background:#0a0a0a}
.login{left:10px;top:484px;width:247px;height:167px;border-radius:8px;background:linear-gradient(#4a4a4a,#232323);border:1px solid #555}
.h-gold{font-family:"Signika",sans-serif;font-weight:700;font-size:22px;color:var(--gold)}
.h-blue{font-family:"Signika",sans-serif;font-weight:700;font-size:21px;color:var(--blue)}
.field{left:22px;width:204px;height:26px;border-radius:13px;background:#111;border:1px solid #444;font-size:13px;color:#777;padding-left:20px;line-height:24px}
.login-btn{left:86px;top:130px;width:70px;height:17px;border-radius:8px;background:linear-gradient(#fff,#bbb);font-size:11px;font-weight:700;color:#222;text-align:center;line-height:17px}
.rule{height:6px;background:var(--rule)}
.list{left:12px;top:716px;width:250px;display:grid;grid-template-columns:128px 122px;row-gap:6px;font-size:12px;color:var(--text)}
.list li{list-style:none;line-height:16px}
.list li::before{content:"⊿ ";font-size:8px;color:#999}
.photo{background:linear-gradient(135deg,#6d4a3a,#2a1f20 50%,#8a7060)}
.dj-row{left:278px;width:672px;height:110px;border-bottom:1px solid #2c2c2c}
.thumb{width:96px;height:86px}
.thumb-a{background:linear-gradient(#e4e4e0,#9aa5aa 60%,#3a4a55)}
.thumb-b{background:linear-gradient(#5aa8d8,#8cc8e8 60%,#c7e6f3)}
.dj-name{font-family:"Signika",sans-serif;font-weight:700;font-size:15px;color:var(--blue)}
.dj-text{font-size:11px;line-height:13px;color:#ddd;margin-top:6px;width:220px}
.more{font-size:11px;font-weight:700;color:var(--blue);margin-top:4px}
.albums{left:278px;top:878px;width:670px;height:258px;background:var(--panel)}
.albums-img{left:10px;top:58px;width:246px;height:186px;background:radial-gradient(circle at 40% 40%,#4a7ab8,#1c2c45 60%,#0d1524)}
.footer{left:0;top:1174px;width:960px;height:114px;background:var(--footer);color:#222;font-size:12px}
.footer-links{left:22px;top:24px;word-spacing:2px}
.footer-base{left:22px;top:46px;display:flex;align-items:center;gap:22px}
.footer-brand{display:flex;align-items:center;gap:6px}
.footer-brand-mark{width:26px;height:26px;border-radius:50%;background:#999}
.footer-brand-name{font-family:"Signika",sans-serif;font-weight:700;font-size:18px;color:#888}
.social{display:flex;gap:8px}
.social span{width:30px;height:30px;border-radius:5px;background:#333}
</style>
</head>
<body>
<div class="stage">
<div class="page">
  <header class="abs header">
    <div class="abs brand">
      <div class="brand-mark"></div>
      <div>
        <div class="brand-name">NOCTURNE</div>
        <div class="brand-sub">ENTERTAINMENT &amp; PRODUCTIONS</div>
      </div>
    </div>
    <div class="abs search">
      <svg width="22" height="20" viewBox="0 0 22 20"><circle cx="8" cy="8" r="6" fill="none" stroke="#999" stroke-width="2.5"/><line x1="12.5" y1="12.5" x2="20" y2="18" stroke="#999" stroke-width="3"/></svg>
      Search
    </div>
  </header>
  <nav class="abs nav">
    <a class="active">HOME</a><a>PROFESSINAL DJS</a><a>WEDDINGS</a><a>PHOTOBOOTH</a><a>LIGHTING DESIGN</a><a>CORPORATE EVENTS</a><a>CONNECT WITH US</a>
  </nav>
  <div class="abs band" style="top:157px"></div>

  <section class="abs hero">
    <div class="abs hero-photo" role="img" aria-label="Young woman listening to music on headphones"></div>
    <div class="abs hero-title-bar"></div>
    <h1 class="abs hero-title">DJ PARTY</h1>
    <p class="abs hero-lead"><span style="font-size:11px">▶</span>&nbsp; The standard chunk of&nbsp; used since the 1500s</p>
    <p class="abs hero-body">The standard chunk of Lorem Ipsum used since the 1500s is reproduced below for those interested. Sections 1.10.32 and 1.10.33 from "de Finibus Bonorum et Malorum" by Aurelo are also reproduced in their exact original form, accompanied by English versions from the 1914 translation by M. Delvaux.</p>
    <svg class="abs" style="left:10px;top:127px" width="40" height="40" viewBox="0 0 40 40"><circle cx="20" cy="20" r="19" fill="#e8e8e8" stroke="#777"/><path d="M25 12 L12 20 L25 28 Z" fill="#555"/></svg>
    <svg class="abs" style="left:910px;top:127px" width="40" height="40" viewBox="0 0 40 40"><circle cx="20" cy="20" r="19" fill="#e8e8e8" stroke="#777"/><path d="M15 12 L28 20 L15 28 Z" fill="#555"/></svg>
    <svg class="abs chev" width="92" height="18" viewBox="0 0 92 18">
      <g fill="none" stroke-width="3"><path d="M2 2l6 7-6 7" stroke="#3cb6e8"/><path d="M16 2l6 7-6 7" stroke="#6ab0c8"/><path d="M30 2l6 7-6 7" stroke="#c6a448"/><path d="M44 2l6 7-6 7" stroke="#f6a01c"/><path d="M58 2l6 7-6 7" stroke="#f6a01c"/><path d="M72 2l6 7-6 7" stroke="#f6a01c"/></g>
    </svg>
  </section>
  <div class="abs band" style="top:465px"></div>

  <main class="abs content"></main>

  <aside>
    <div class="abs login">
      <h2 class="abs h-gold" style="left:20px;top:6px">LOG IN</h2>
      <div class="abs field" style="top:45px">username</div>
      <div class="abs field" style="top:87px">password</div>
      <div class="abs login-btn">LOG IN</div>
    </div>
    <h2 class="abs h-gold" style="left:13px;top:664px">PHOTOBOOTH</h2>
    <div class="abs rule" style="left:10px;top:697px;width:249px"></div>
    <ul class="abs list">
      <li><u>Bar / Bat Mitzvahs</u></li><li>Fraternity / Sorority</li>
      <li>Birthdays</li><li>Fundraisers</li>
      <li>Charity</li><li>High School Proms</li>
      <li>Class Reunions</li><li>Quinceaneras</li>
      <li>Corporate Events</li><li>Special Events</li>
      <li>Expos</li><li>Weddings</li>
    </ul>
    <h2 class="abs h-gold" style="left:13px;top:874px">WEDDING</h2>
    <div class="abs rule" style="left:10px;top:907px;width:249px"></div>
    <svg class="abs" style="left:14px;top:980px" width="12" height="16"><path d="M10 0 L0 8 L10 16Z" fill="#aaa"/></svg>
    <div class="abs photo" style="left:32px;top:928px;width:204px;height:118px" role="img" aria-label="Guests dancing at a wedding reception"></div>
    <svg class="abs" style="left:242px;top:980px" width="12" height="16"><path d="M2 0 L12 8 L2 16Z" fill="#aaa"/></svg>
    <p class="abs" style="left:17px;top:1058px;width:240px;font-size:11px;line-height:16.5px;color:#ccc">The standard chunk of Lorem Ipsum used since the 1500s is reproduced below for those interested. Sections 1.10.32 and 1.10.33 from Finibus Bonorum et Malorum.</p>
  </aside>

  <section>
    <h2 class="abs h-blue" style="left:277px;top:486px">PROFESSINAL DJS</h2>
    <div class="abs rule" style="left:277px;top:520px;width:673px"></div>

    <div class="abs dj-row" style="top:536px">
      <div class="abs thumb thumb-a" style="left:2px;top:7px" role="img" aria-label="Album cover with a pier over calm water"></div>
      <div class="abs" style="left:104px;top:6px"><div class="dj-name">M. Delvaux</div><p class="dj-text">The standard chunk of used since the 1500s is reproduced below for those interested. Sections 1.10.32 and 1.10.33</p><p class="more">Know more ▸</p></div>
      <div class="abs thumb thumb-b" style="left:362px;top:7px" role="img" aria-label="Blue album cover with a city skyline"></div>
      <div class="abs" style="left:471px;top:6px"><div class="dj-name">M. Delvaux</div><p class="dj-text" style="width:200px">The standard chunk of used since the 1500s is reproduced below for those interested. Sections 1.10.32 and 1.10.33</p><p class="more">Know more ▸</p></div>
    </div>
    <div class="abs dj-row" style="top:647px">
      <div class="abs thumb thumb-a" style="left:2px;top:7px" role="img" aria-label="Album cover with a pier over calm water"></div>
      <div class="abs" style="left:104px;top:6px"><div class="dj-name">M. Delvaux</div><p class="dj-text">The standard chunk of used since the 1500s is reproduced below for those interested. Sections 1.10.32 and 1.10.33</p><p class="more">Know more ▸</p></div>
      <div class="abs thumb thumb-b" style="left:362px;top:7px" role="img" aria-label="Blue album cover with a city skyline"></div>
      <div class="abs" style="left:471px;top:6px"><div class="dj-name">M. Delvaux</div><p class="dj-text" style="width:200px">The standard chunk of used since the 1500s is reproduced below for those interested. Sections 1.10.32 and 1.10.33</p><p class="more">Know more ▸</p></div>
    </div>
    <div class="abs dj-row" style="top:758px">
      <div class="abs thumb thumb-a" style="left:2px;top:7px" role="img" aria-label="Album cover with a pier over calm water"></div>
      <div class="abs" style="left:104px;top:6px"><div class="dj-name">M. Delvaux</div><p class="dj-text">The standard chunk of used since the 1500s is reproduced below for those interested. Sections 1.10.32 and 1.10.33</p><p class="more">Know more ▸</p></div>
      <div class="abs thumb thumb-b" style="left:362px;top:7px" role="img" aria-label="Blue album cover with a city skyline"></div>
      <div class="abs" style="left:471px;top:6px"><div class="dj-name">M. Delvaux</div><p class="dj-text" style="width:200px">The standard chunk of used since the 1500s is reproduced below for those interested. Sections 1.10.32 and 1.10.33</p><p class="more">Know more ▸</p></div>
    </div>

    <div class="abs albums">
      <h2 class="abs h-blue" style="left:15px;top:8px">OUR ALBUMS</h2>
      <div class="abs rule" style="left:10px;top:38px;width:650px"></div>
      <div class="abs albums-img" role="img" aria-label="DJ in a cap performing at turntables"></div>
      <p class="abs" style="left:266px;top:58px;width:390px;font-size:14px;line-height:19px;color:var(--blue)">The standard chunk of used since the 1500s is reproduced below for those interested.</p>
      <p class="abs" style="left:265px;top:102px;width:395px;font-size:11px;line-height:16.5px;color:#bbb">The standard chunk of Lorem Ipsum used since the 1500s is reproduced below for those interested.Contrary to popular belief, Lorem Ipsum is not simply random text. It has roots in a piece of classical Latin literature from 45 BC. Sections 1.10.32 and 1.10.33 from "de Finibus Bonorum et Malorum" by Aurelo are also reproduced in their exact original form, accompanied by English versions from the 1914 translation by M. Delvaux.Contrary to popular belief, Lorem Ipsum is not simply random text.</p>
      <div class="abs" style="left:543px;top:226px;width:112px;height:22px;background:#000;color:#fff;font-size:12px;line-height:22px;padding-left:10px;clip-path:polygon(0 0,90% 0,100% 50%,90% 100%,0 100%)">READ MORE&gt;&gt;</div>
    </div>
  </section>

  <footer class="abs footer">
    <p class="abs footer-links">Home &nbsp;| &nbsp;Professional DJs &nbsp;| &nbsp;Weddings &nbsp;| &nbsp;Photobooth &nbsp;| &nbsp;Lighting Design &nbsp;| &nbsp;Corporate Events &nbsp;| &nbsp;Log in</p>
    <div class="abs footer-base">
      <p>Copyright @ 2011 www.nocturne-events.com All rights reserved</p>
      <div class="footer-brand">
        <span class="footer-brand-mark"></span>
        <span class="footer-brand-name">NOCTURNE</span>
      </div>
    </div>
    <p class="abs" style="left:759px;top:24px">Connect with US :</p>
    <div class="abs social" style="left:759px;top:42px"><span></span><span></span><span></span><span></span><span></span></div>
  </footer>
</div>
</div>
</body>
</html>
```